Postcard Design

We need a postcard design for our 10 year anniversary open house. The company is Fernwood Medical Spa. The web site is www.fernwoodmedicalspa.com. We want royal blue, sliver and white colors for the postcard along with a 10 Year image.

It Company

```html
<!DOCTYPE html>
<html lang="en">
<head>
<meta charset="utf-8">
<title>Fernwood Medical Spa – 10 Year Anniversary Open House</title>
<link rel="stylesheet" href="https://fonts.googleapis.com/css2?family=Anton&family=Open+Sans:wght@400&display=swap">
<style>
  :root {
    --royal-blue: #0b47a5;
    --silver: #c9ccc8;
    --white: #ffffff;
    --sky-light: #e6effa;
    --sky-mid: #a9c4e4;
    --sky-deep: #6f93c4;
  }
  html, body {
    margin: 0;
    padding: 0;
    width: 1200px;
    height: 811px;
    overflow: hidden;
    background: var(--white);
  }
  .postcard { display: block; width: 1200px; height: 811px; }
  .band { fill: var(--royal-blue); }
  .card-body { fill: var(--silver); }
  .feature-panel { fill: var(--royal-blue); }
  .ribbon { fill: var(--royal-blue); }
  .brand-name {
    font-family: "Open Sans", sans-serif;
    font-weight: 400;
    font-size: 36px;
    fill: var(--royal-blue);
  }
  .brand-mark { fill: var(--royal-blue); }
  .brand-rule { stroke: var(--royal-blue); stroke-width: 1.2; }
  .brand-line {
    font-family: "Open Sans", sans-serif;
    fill: var(--royal-blue);
    text-anchor: middle;
  }
  .brand-line--main { font-size: 15px; }
  .brand-line--sub { font-size: 11.5px; }
  .headline {
    font-family: "Anton", sans-serif;
    fill: var(--white);
    stroke: var(--royal-blue);
    stroke-width: 1.5;
    paint-order: stroke;
  }
  .headline--lead { font-size: 37px; }
  .headline--ribbon { font-size: 36px; stroke: none; }
  .contact {
    font-family: "Open Sans", sans-serif;
    font-size: 13px;
    fill: var(--royal-blue);
  }
  .footer-links {
    font-family: "Open Sans", sans-serif;
    font-size: 13px;
    fill: var(--white);
    text-anchor: middle;
  }
</style>
</head>
<body>
<svg class="postcard" viewBox="0 0 1200 811" xmlns="http://www.w3.org/2000/svg">
  <defs>
    <linearGradient id="blossom-tones" x1="0" y1="0" x2="1" y2="1">
      <stop offset="0" stop-color="var(--sky-mid)"/>
      <stop offset="0.45" stop-color="var(--sky-light)"/>
      <stop offset="1" stop-color="var(--sky-deep)"/>
    </linearGradient>
  </defs>

  <!-- card -->
  <rect class="card-body" x="248" y="135" width="700" height="538"/>
  <rect class="band band--top" x="248" y="135" width="700" height="40"/>
  <rect class="band band--bottom" x="248" y="633" width="700" height="40"/>

  <!-- feature panel -->
  <path class="feature-panel" d="M457,182 H824 A58,58 0 0 1 882,240 V626 H524 A67,67 0 0 1 457,559 Z"/>

  <!-- blossom photo area -->
  <path role="img" aria-label="Photo of pale blue spring blossoms on branches against a light sky"
        fill="url(#blossom-tones)"
        d="M470,261 H838 A33,33 0 0 1 871,294 V548 H503 A33,33 0 0 1 470,515 Z"/>

  <!-- brand -->
  <circle class="brand-mark" cx="349" cy="222" r="12"/>
  <text class="brand-name" x="349" y="281" text-anchor="middle">Fernwood</text>
  <text class="brand-line brand-line--main" x="349" y="305">Medical Spa</text>
  <line class="brand-rule" x1="277" y1="309" x2="421" y2="309"/>
  <text class="brand-line brand-line--sub" x="349" y="321">Cosmetic &amp; Laser Services</text>

  <!-- headline -->
  <text class="headline headline--lead" x="479" y="366" textLength="230" lengthAdjust="spacingAndGlyphs">JOIN US FOR OUR</text>

  <!-- ribbon -->
  <polygon class="ribbon" points="402,373 457,396 457,452 402,440 432,412"/>
  <polygon class="ribbon" points="892,377 936,394 914,421 936,452 883,429"/>
  <path class="ribbon" d="M448,400 C560,420 640,385 720,370 C790,358 850,362 890,362 L890,425 C850,425 790,420 720,432 C640,447 560,470 448,463 Z"/>
  <text class="headline headline--ribbon" x="514" y="452" transform="rotate(-13 514 452)" textLength="312" lengthAdjust="spacingAndGlyphs">10 YEAR ANNIVERSARY</text>

  <text class="headline headline--lead" x="692" y="470" textLength="174" lengthAdjust="spacingAndGlyphs">OPEN HOUSE</text>

  <!-- contact -->
  <text class="contact" x="272" y="554">Ph: 702.555.0142</text>
  <text class="contact" x="272" y="569">Fax: 702.555.0187</text>
  <text class="contact" x="272" y="584">1840 N. Alder Dr., Suite 210</text>
  <text class="contact" x="272" y="599">Las Vegas, NV 89100</text>

  <text class="footer-links" x="598" y="655">www.fernwoodmedicalspa.com; fernwoodmedicalspa@mail.com</text>
</svg>
</body>
</html>
```